Business Card Design for Software Development Company

I am looking for a business card design the incorporates my new logo (attached below).

Key information to include:
Name: Marcus Delvine
Title: CEO
Email: marcus@brightwellcivic.com
Phone: 555-218-4093
Website: www.brightwellcivic.com

NOTE: This design should be easy to edit so that we can order cards for different members of our team.

```html
<!DOCTYPE html>
<html lang="en">
<head>
<meta charset="utf-8">
<title>Brightwell Labs – Business Card</title>
<link rel="stylesheet" href="https://fonts.googleapis.com/css2?family=Montserrat:wght@400;500;600;700&display=swap">
<style>
  :root {
    --page-bg: #e4e2e5;
    --card-front: #ffffff;
    --card-back: #6e779b;
    --ink: #1f2233;
    --brand-navy: #363b55;
    --accent: #e8793a;
    --facet-light: #a9b3d6;
    --facet-dark: #474d6a;
    --white: #ffffff;
  }
  * { box-sizing: border-box; margin: 0; padding: 0; }
  html, body {
    width: 1200px; height: 1108px; overflow: hidden;
    background: var(--page-bg);
    font-family: "Montserrat", sans-serif;
    color: var(--ink);
  }
  .card {
    position: absolute;
    left: 229px;
    width: 756px;
  }
  .card--front { top: 56px; height: 461px; background: var(--card-front); }
  .card--back { top: 575px; height: 444px; background: var(--card-back); overflow: hidden; }

  .brand-name {
    position: absolute;
    font-weight: 600;
    letter-spacing: -0.5px;
    white-space: nowrap;
  }
  .card--front .brand-name {
    left: 92px; top: 240px;
    font-size: 31px;
    color: var(--brand-navy);
  }
  .divider {
    position: absolute;
    left: 373px; top: 178px;
    width: 1px; height: 146px;
    background: var(--accent);
  }
  .contact {
    position: absolute;
    left: 387px; top: 176px;
    list-style: none;
  }
  .contact__name {
    font-size: 28px; font-weight: 600;
    color: var(--accent);
    line-height: 1.2;
  }
  .contact__title { font-size: 16px; margin: 2px 0 4px; }
  .contact__row {
    display: flex; align-items: center; gap: 8px;
    font-size: 17px; height: 29px;
  }
  .contact__row svg { width: 15px; height: 15px; flex: none; }
  .address {
    position: absolute;
    left: 0; right: 0; top: 396px;
    text-align: center;
    font-size: 16.5px;
  }

  .facet-art {
    position: absolute;
    left: 308px; top: 33px;
    width: 448px; height: 411px;
  }
  .card--back .brand-name {
    left: 28px; top: 318px;
    font-size: 56px;
    font-weight: 700;
    color: var(--white);
  }
</style>
</head>
<body>
  <section class="card card--front">
    <span class="brand-name">Brightwell Labs</span>
    <span class="divider"></span>
    <ul class="contact">
      <li class="contact__name">Marcus Delvine</li>
      <li class="contact__title">CEO</li>
      <li class="contact__row">
        <svg viewBox="0 0 16 16" aria-hidden="true"><path d="M3.5 1.5l2.5 3-1.5 1.8c.8 1.8 2.4 3.4 4.2 4.2L10.5 9l3 2.5-1.5 2.5C6.5 14 2 9.5 1.5 3z" fill="none" stroke="var(--accent)" stroke-width="1.5" stroke-linejoin="round"/></svg>
        555-218-4093
      </li>
      <li class="contact__row">
        <svg viewBox="0 0 16 16" aria-hidden="true"><rect x="1.5" y="3.5" width="13" height="9" fill="var(--accent)"/><path d="M1.5 3.5L8 9l6.5-5.5" fill="none" stroke="#fff" stroke-width="1.2"/></svg>
        marcus@brightwellcivic.com
      </li>
      <li class="contact__row">
        <svg viewBox="0 0 16 16" aria-hidden="true"><circle cx="8" cy="8" r="7" fill="var(--accent)"/><path d="M1 8h14M8 1c-3 3.5-3 10.5 0 14M8 1c3 3.5 3 10.5 0 14" fill="none" stroke="#fff" stroke-width="1"/></svg>
        www.brightwellcivic.com
      </li>
    </ul>
    <p class="address">418 Harbor Lane, #112 Fairmont, OH 43099</p>
  </section>

  <section class="card card--back">
    <svg class="facet-art" role="img" aria-label="Large faceted brand-symbol decoration in slate blue tones" viewBox="0 0 448 411" preserveAspectRatio="none">
      <defs>
        <linearGradient id="facetFill" x1="0" y1="0" x2="1" y2="0.6">
          <stop offset="0" stop-color="var(--facet-light)"/>
          <stop offset="0.55" stop-color="var(--facet-dark)"/>
          <stop offset="1" stop-color="var(--facet-dark)"/>
        </linearGradient>
      </defs>
      <rect width="448" height="411" fill="url(#facetFill)" opacity="0.85"/>
    </svg>
    <span class="brand-name">Brightwell Labs</span>
  </section>
</body>
</html>
```